Infectious Diseases Research Laboratory Needs Business Card

We need a business card for an academic research laboratory based in Kansas City called MORVEK. The full lab name is Microbial Dose-Response/Exposure Bridging Studies Laboratory, but this does not need to be incorporated. We study novel ways to optimize the treatment of multidrug-resistant bacterial infections ("superbugs") throughout the entire biomedical research spectrum (from benchtop to bedside). The name MORVEK is not only an acronym for our lab name, but also represents our desire to make discoveries and explore the unknown (the stars, if you well). It also serves as an ode to the state of Kansas motto where we are based, ad astra per aspera ("to the stars, through difficulty").

Target Market(s)

Pharmaceutical companies, researchers

Industry/Entity Type

Pharmaceutical

Contact Information for Business Card

The business card should incorporate and complement our new logo (see uploaded files). Double-sided designs are preferred. Looking for something modern, but professional.

Font styles to use
Sans Serif

Requirements
Must have
• Double-sided. One side would ideally be a solid color incorporating logo and the other should also have the logo (smaller), but incorporate staff information.
• Color codes:
• Red: #F04C51
• Blue: #3477B5
• Gray: #808285

```html
<!DOCTYPE html>
<html lang="en">
<head>
<meta charset="utf-8">
<title>MORVEK Business Card</title>
<link href="https://fonts.googleapis.com/css2?family=Jost:wght@400;500&family=Roboto+Condensed:wght@500&display=swap" rel="stylesheet">
<style>
  :root {
    --red: #F04C51;
    --blue: #3477B5;
    --blue-deep: #2a67a3;
    --gray: #808285;
    --ink: #4a4a4c;
    --stage: #2a2a2b;
    --paper: #ffffff;
    --paper-shade: #e2e2e3;
  }
  * { margin: 0; padding: 0; box-sizing: border-box; }
  html, body { width: 1200px; height: 960px; overflow: hidden; }
  body {
    position: relative;
    background: var(--stage);
    font-family: "Jost", "Helvetica Neue", Arial, sans-serif;
    color: var(--ink);
  }
  .card {
    position: absolute;
    width: 600px;
    height: 342px;
    border-radius: 22px;
    overflow: hidden;
  }
  .card-front {
    left: 302px; top: 129px;
    background: linear-gradient(90deg, var(--paper-shade) 0%, #f3f3f3 30%, var(--paper) 50%);
  }
  .card-back {
    left: 299px; top: 488px;
    background: linear-gradient(90deg, var(--blue-deep) 0%, var(--blue) 100%);
  }
  .brand {
    position: absolute;
    right: 32px; top: 48px;
    display: flex; align-items: center; gap: 14px;
  }
  .brand-dot {
    width: 44px; height: 44px; border-radius: 50%;
    background: var(--blue);
  }
  .brand-name {
    font-family: "Jost", "Helvetica Neue", Arial, sans-serif;
    font-weight: 500;
    font-size: 50px;
    line-height: 1;
    letter-spacing: 2px;
    color: var(--red);
  }
  .staff { position: absolute; left: 28px; top: 174px; }
  .staff-name {
    font-family: "Roboto Condensed", "Arial Narrow", sans-serif;
    font-weight: 500;
    font-size: 24px;
    line-height: 1;
    color: var(--blue);
  }
  .staff-role {
    margin-top: 5px;
    font-size: 15px;
    line-height: 1;
    color: var(--red);
    letter-spacing: 0.3px;
  }
  .divider {
    position: absolute;
    left: 28px; right: 32px; top: 228px;
    height: 1px;
    background: var(--gray);
  }
  .contact-list {
    position: absolute; left: 28px; top: 243px;
    list-style: none;
  }
  .contact-list li {
    display: flex; align-items: center; gap: 8px;
    height: 19px;
    font-size: 15px;
    color: var(--ink);
  }
  .contact-list svg { width: 15px; height: 15px; fill: var(--blue); flex: none; }
  .contact-list li.email { font-size: 14px; }
  .address {
    position: absolute; right: 32px; top: 262px;
    text-align: right;
    font-size: 14px;
    line-height: 18px;
    color: var(--ink);
  }
  .back-brand {
    position: absolute;
    left: 0; right: 0; top: 124px;
    display: flex; justify-content: center; align-items: center; gap: 18px;
  }
  .back-brand .brand-dot { width: 62px; height: 62px; background: var(--paper); }
  .back-brand .brand-name { color: var(--paper); font-size: 64px; }
  .back-web {
    position: absolute; left: 0; right: 0; top: 284px;
    text-align: center;
    font-size: 15px;
    letter-spacing: 4.5px;
    color: var(--paper);
  }
</style>
</head>
<body>
  <section class="card card-front">
    <div class="brand">
      <span class="brand-dot"></span>
      <span class="brand-name">MORVEK</span>
    </div>
    <div class="staff">
      <h1 class="staff-name">ELENA VARGA</h1>
      <p class="staff-role">CEO/FOUNDER</p>
    </div>
    <div class="divider"></div>
    <ul class="contact-list">
      <li><svg viewBox="0 0 16 16" aria-hidden="true"><path d="M3.5 1 6 3.8 4.7 5.6c.8 1.9 2.2 3.4 4.1 4.3l1.6-1.4L13.5 11l-1.2 2.8c-5.5-.2-10-4.9-10.2-10.3z"/></svg>816 555 0142</li>
      <li><svg viewBox="0 0 16 16" aria-hidden="true"><path d="M4.5 1h7v14h-7zM6 3v9h4V3zm1.5 10.2h1v1h-1z" fill-rule="evenodd"/></svg>816 555 0187</li>
      <li><svg viewBox="0 0 16 16" aria-hidden="true"><path d="M4 1h8v4H4zM1 6h14v6h-2v-2H3v2H1zm3 5h8v4H4z"/></svg>816 555 0163</li>
      <li class="email"><svg viewBox="0 0 16 16" aria-hidden="true"><path d="M1 3.5h14v10H1zm1.3 1.2v.4L8 9l5.7-3.9v-.4zm0 1.9v5.7h11.4V6.6L8 10.5z" fill-rule="evenodd"/></svg>e.varga@morveklab.org</li>
    </ul>
    <address class="address" style="font-style:normal">
      2410 Linden Court<br>
      Kansas City, Kansas 66160<br>
      www.morveklab.org
    </address>
  </section>

  <section class="card card-back">
    <div class="back-brand">
      <span class="brand-dot"></span>
      <span class="brand-name">MORVEK</span>
    </div>
    <p class="back-web">WWW.MORVEK.ORG</p>
  </section>
</body>
</html>
```